The Copperwell

We need a APP for our members. this is a Private Bar/Venue. history of the brick building is it was built in1898 and was a gentleman club, oyster house, cigar factory and then law offices before we purchased and are beginning restoration.
the APP must include
1. direct texting to the concierge
2. calendar of events
3. vantor Lock To open the lock, anyone with a code can approach the door, enable their phone's Bluetooth and press the relevant address from the app.
Read more: http://www.evenpostgazette.co.uk/sciencetech/article-4418206/farewell-metal-keys-phone-bolt-opens-front-door-without-anything-in-hand.html#ixzz9kQR2mpaL
4. Menus from various restaurants from our surrounding area
5. member name and member number to give the feel that the app is personalized
6. the members account balance
7. ability to pay their bill with credit card or quid line monthly and automatically.
8. link to züro with its own icon within the app.
9.the ability to reserve the room
Anything else that may of interest for our members that may be relevant that I may not have mentioned since we are new at this...
35 to 60 years of age
Club

```html
<!DOCTYPE html>
<html lang="en">
<head>
<meta charset="utf-8">
<title>The Copperwell – Messages</title>
<link rel="stylesheet" href="https://fonts.googleapis.com/css2?family=Questrial&display=swap">
<style>
  :root {
    --cyan: #17d1ef;
    --cyan-pale: #c9f6fb;
    --wall: #121212;
    --wall-deep: #070707;
    --card: #ffffff;
    --rule: #e2e2e2;
    --name: #a8a8a8;
    --meta: #b0b0b0;
    --input: #dcdcdc;
    --input-text: #a8a8a8;
    --tabbar: #0b0b0b;
    --avatar-a: #7b6a5c;
    --avatar-b: #5e6f78;
  }
  * { box-sizing: border-box; margin: 0; padding: 0; }
  html, body { width: 675px; height: 1200px; overflow: hidden; }
  body {
    position: relative;
    font-family: "Questrial", "Helvetica Neue", Arial, sans-serif;
    background: var(--wall);
  }
  .wall {
    position: absolute; inset: 0;
    background: radial-gradient(ellipse at 50% 35%, #1d1d1d 0%, var(--wall) 55%, var(--wall-deep) 100%);
  }
  .top-bar svg { position: absolute; }
  .back { left: 76px; top: 96px; }
  .menu { left: 302px; top: 60px; filter: drop-shadow(0 4px 4px rgba(0,0,0,.7)); }
  .chat { left: 554px; top: 79px; }

  .messages-card {
    position: absolute; left: 32px; top: 220px; width: 612px; height: 869px;
    background: var(--card);
    border-radius: 20px 20px 0 0;
    overflow: hidden;
  }
  .messages-card::after {
    content: ""; position: absolute; left: 0; right: 0; bottom: 0; height: 26px;
    background: linear-gradient(to bottom, rgba(255,255,255,0), rgba(20,20,20,.9));
  }
  .card-header { position: relative; height: 100px; border-bottom: 1px solid var(--rule); }
  .card-header .title {
    position: absolute; left: 0; right: 0; top: 34px; text-align: center;
    color: var(--cyan); font-size: 30px; font-weight: 400; letter-spacing: 1.5px; line-height: 36px;
  }
  .card-header svg { position: absolute; }
  .search { left: 55px; top: 36px; }
  .compose { left: 546px; top: 35px; }

  .thread { position: absolute; left: 0; width: 612px; height: 80px; }
  .thread .tick { position: absolute; left: 25px; top: 23px; }
  .thread .avatar {
    position: absolute; left: 81px; top: 9px; width: 62px; height: 62px; border-radius: 50%;
    background: radial-gradient(circle at 45% 40%, var(--avatar-a), var(--avatar-b));
  }
  .thread .name {
    position: absolute; left: 165px; top: 20px; font-size: 30px; line-height: 36px;
    color: var(--name); letter-spacing: 1.5px; white-space: nowrap;
  }
  .thread .time {
    position: absolute; right: 30px; top: 30px; font-size: 15px; line-height: 18px;
    color: var(--meta); letter-spacing: .8px; white-space: nowrap;
  }
  .rule { position: absolute; left: 98px; width: 417px; height: 1px; background: var(--rule); }

  .broadcast {
    position: absolute; left: 52px; top: 758px; width: 539px; height: 57px;
    border-radius: 29px; background: var(--input);
    color: var(--input-text); font-size: 15px; line-height: 57px; padding-left: 30px; letter-spacing: .6px;
    white-space: nowrap;
  }
  .pin { position: absolute; left: 213px; top: 829px; display: flex; align-items: center; gap: 10px;
    font-size: 16px; color: #6f6f6f; letter-spacing: 1px; }
  .send {
    position: absolute; left: 431px; top: 824px; width: 159px; height: 29px; border-radius: 15px;
    background: linear-gradient(to right, #dff8fc, #8fe9f7);
    color: #5f7f86; font-size: 16px; text-align: center; line-height: 29px; letter-spacing: 1px;
  }

  .tab-bar {
    position: absolute; left: 0; top: 1092px; width: 675px; height: 108px; background: var(--tabbar);
  }
  .tab-bar svg { position: absolute; top: 25px; }
  .ride-link {
    position: absolute; left: 572px; top: 25px; width: 70px; height: 56px;
    display: flex; align-items: center; justify-content: center;
    color: var(--cyan); font-size: 22px; letter-spacing: 1px;
  }
</style>
</head>
<body>
  <div class="wall" role="img" aria-label="Dark brick wall background"></div>

  <header class="top-bar">
    <svg class="back" width="52" height="36" viewBox="0 0 52 36" aria-label="Back">
      <path d="M48 18H6M20 4L5 18l15 14" fill="none" stroke="var(--cyan)" stroke-width="5" stroke-linecap="round" stroke-linejoin="round"/>
    </svg>
    <svg class="menu" width="70" height="92" viewBox="0 0 70 92" aria-label="Menu">
      <rect x="2" y="3" width="66" height="13" fill="var(--cyan-pale)"/>
      <rect x="2" y="40" width="66" height="13" fill="var(--cyan-pale)"/>
      <rect x="2" y="75" width="66" height="13" fill="var(--cyan-pale)"/>
    </svg>
    <svg class="chat" width="64" height="62" viewBox="0 0 64 62" aria-label="Concierge chat">
      <path d="M3 4h44v30H18l-10 9v-9H3z" fill="none" stroke="var(--cyan)" stroke-width="3" stroke-linejoin="round"/>
      <path d="M47 16h13v30h-5v12l-12-12H22V34" fill="none" stroke="var(--cyan)" stroke-width="3" stroke-linejoin="round"/>
      <circle cx="15" cy="19" r="2.5" fill="var(--cyan)"/><circle cx="25" cy="19" r="2.5" fill="var(--cyan)"/><circle cx="35" cy="19" r="2.5" fill="var(--cyan)"/>
    </svg>
  </header>

  <main class="messages-card">
    <div class="card-header">
      <svg class="search" width="34" height="34" viewBox="0 0 34 34" aria-label="Search">
        <circle cx="13" cy="13" r="10" fill="none" stroke="var(--cyan)" stroke-width="3.5"/>
        <path d="M20.5 20.5L31 31" stroke="var(--cyan)" stroke-width="4" stroke-linecap="round"/>
      </svg>
      <h1 class="title">Messege</h1>
      <svg class="compose" width="36" height="36" viewBox="0 0 36 36" aria-label="New message">
        <circle cx="18" cy="18" r="16" fill="none" stroke="var(--cyan)" stroke-width="3"/>
        <path d="M18 9v18M9 18h18" stroke="var(--cyan)" stroke-width="3"/>
      </svg>
    </div>

    <div class="thread" style="top:106px">
      <svg class="tick" width="34" height="34" viewBox="0 0 34 34"><path d="M31 15a15 15 0 1 1-6-11" fill="none" stroke="var(--cyan)" stroke-width="3" stroke-linecap="round"/><path d="M10 16l6 6 14-15" fill="none" stroke="var(--cyan)" stroke-width="3" stroke-linecap="round" stroke-linejoin="round"/></svg>
      <div class="avatar" role="img" aria-label="Member portrait"></div>
      <span class="name">Colette Branwell</span><span class="time">Just now</span>
    </div>
    <div class="rule" style="top:202px"></div>

    <div class="thread" style="top:220px">
      <svg class="tick" width="34" height="34" viewBox="0 0 34 34"><path d="M31 15a15 15 0 1 1-6-11" fill="none" stroke="var(--cyan)" stroke-width="3" stroke-linecap="round"/><path d="M10 16l6 6 14-15" fill="none" stroke="var(--cyan)" stroke-width="3" stroke-linecap="round" stroke-linejoin="round"/></svg>
      <div class="avatar" role="img" aria-label="Member portrait"></div>
      <span class="name">Owen Halbrecht</span><span class="time">Just now</span>
    </div>
    <div class="rule" style="top:318px"></div>

    <div class="thread" style="top:335px">
      <svg class="tick" width="34" height="34" viewBox="0 0 34 34"><path d="M31 15a15 15 0 1 1-6-11" fill="none" stroke="var(--cyan)" stroke-width="3" stroke-linecap="round"/><path d="M10 16l6 6 14-15" fill="none" stroke="var(--cyan)" stroke-width="3" stroke-linecap="round" stroke-linejoin="round"/></svg>
      <div class="avatar" role="img" aria-label="Member portrait"></div>
      <span class="name">Felix Dunmarrow</span><span class="time">18:30pm</span>
    </div>
    <div class="rule" style="top:434px"></div>

    <div class="thread" style="top:449px">
      <svg class="tick" width="34" height="34" viewBox="0 0 34 34"><path d="M31 15a15 15 0 1 1-6-11" fill="none" stroke="var(--cyan)" stroke-width="3" stroke-linecap="round"/><path d="M10 16l6 6 14-15" fill="none" stroke="var(--cyan)" stroke-width="3" stroke-linecap="round" stroke-linejoin="round"/></svg>
      <div class="avatar" role="img" aria-label="Member portrait"></div>
      <span class="name">Simon Rovet</span><span class="time">1hr ago</span>
    </div>
    <div class="rule" style="top:550px"></div>

    <div class="thread" style="top:564px">
      <svg class="tick" width="34" height="34" viewBox="0 0 34 34"><path d="M31 15a15 15 0 1 1-6-11" fill="none" stroke="var(--cyan)" stroke-width="3" stroke-linecap="round"/><path d="M10 16l6 6 14-15" fill="none" stroke="var(--cyan)" stroke-width="3" stroke-linecap="round" stroke-linejoin="round"/></svg>
      <div class="avatar" role="img" aria-label="Member portrait"></div>
      <span class="name">Marisa Tolvenk</span><span class="time">2hr ago</span>
    </div>
    <div class="rule" style="top:659px"></div>

    <div class="thread" style="top:679px">
      <svg class="tick" width="34" height="34" viewBox="0 0 34 34"><path d="M31 15a15 15 0 1 1-6-11" fill="none" stroke="var(--cyan)" stroke-width="3" stroke-linecap="round"/><path d="M10 16l6 6 14-15" fill="none" stroke="var(--cyan)" stroke-width="3" stroke-linecap="round" stroke-linejoin="round"/></svg>
      <div class="avatar" role="img" aria-label="Member portrait"></div>
      <span class="name">Lucas Prior</span><span class="time">30min ago</span>
    </div>

    <div class="broadcast">We are finishing early today, Next party will be notify soon.</div>
    <label class="pin">
      <svg width="20" height="20" viewBox="0 0 20 20"><path d="M17 9v9H2V3h11" fill="none" stroke="var(--cyan)" stroke-width="2"/><path d="M6 9l4 4 9-11" fill="none" stroke="var(--cyan)" stroke-width="2"/></svg>
      Pin to all members
    </label>
    <div class="send">SEND</div>
  </main>

  <nav class="tab-bar">
    <svg style="left:39px" width="56" height="56" viewBox="0 0 56 56" aria-label="Events calendar">
      <rect x="2" y="6" width="52" height="48" rx="3" fill="none" stroke="var(--cyan)" stroke-width="3"/>
      <path d="M2 16h52" stroke="var(--cyan)" stroke-width="3"/>
      <path d="M9 2v9M16 2v9M23 2v9M30 2v9M37 2v9M44 2v9" stroke="var(--cyan)" stroke-width="2.5"/>
      <text x="28" y="46" text-anchor="middle" font-family="Questrial, sans-serif" font-size="24" fill="var(--cyan)">23</text>
    </svg>
    <svg style="left:176px" width="56" height="56" viewBox="0 0 56 56" aria-label="Restaurant menus">
      <path d="M6 50L44 12c3-3 8-2 8 2c0 4-4 8-9 10L12 54z" fill="none" stroke="var(--cyan)" stroke-width="4" stroke-linejoin="round"/>
      <path d="M50 52L22 24" stroke="var(--cyan)" stroke-width="5" stroke-linecap="round"/>
      <path d="M22 24L6 8M26 20L12 4M18 28L4 14M6 8" stroke="var(--cyan)" stroke-width="3.5" stroke-linecap="round"/>
    </svg>
    <svg style="left:320px" width="34" height="60" viewBox="0 0 34 60" aria-label="Account balance">
      <path d="M28 14c-2-4-6-6-11-6-6 0-11 3-11 9 0 12 22 8 22 20 0 6-5 9-11 9-6 0-10-2-12-6" fill="none" stroke="var(--cyan)" stroke-width="4" stroke-linecap="round"/>
      <path d="M15 2v56M20 2v56" stroke="var(--cyan)" stroke-width="2.5"/>
    </svg>
    <svg style="left:444px" width="58" height="58" viewBox="0 0 58 58" aria-label="Door lock">
      <rect x="2" y="2" width="26" height="54" rx="3" fill="none" stroke="var(--cyan)" stroke-width="3"/>
      <rect x="30" y="2" width="26" height="54" rx="3" fill="none" stroke="var(--cyan)" stroke-width="3"/>
      <rect x="10" y="10" width="10" height="22" rx="5" fill="none" stroke="var(--cyan)" stroke-width="3"/>
      <rect x="38" y="10" width="10" height="22" rx="5" fill="none" stroke="var(--cyan)" stroke-width="3"/>
      <circle cx="15" cy="44" r="4" fill="none" stroke="var(--cyan)" stroke-width="3"/>
      <circle cx="43" cy="44" r="4" fill="none" stroke="var(--cyan)" stroke-width="3"/>
    </svg>
    <a class="ride-link">züro</a>
  </nav>
</body>
</html>
```